BROCHURE OR FLYER PLEASE

We need a brochure design for our company TV Surfacing Contractors Limited. Our website is www.tvsurfacing-demo.co.nz. We have rented a 3m permanent booth at the dwelling plans hub in central Auckland. Their website is: www.dwellingplans-demo.co.nz
We need to design and provide a company brochure outlining who we are, and the types of services we provide. Half of our flooring business is dedicated to basically Polished Concrete/Concrete Grinding; and the other half to resin and other floor toppings. We are based in Auckland, NZ and will be marketing to existing and new home owners essentially in Auckland. We want to contain concise information on our services and present this in a professional but sheik style. Housing in NZ is expensive so our brochure needs to be up market and user friendly. Polished concrete is more expensive that carpet so I feel it is important to list the benefits etc. I will attach our website and information regarding our products. We would like a double sided brochure. Our company colours are blue/red/black. I have attached some photo's you are welcome to use. Please refer to our website for more information www.tvsurfacing-demo.co.nz. Thank you.

Target Market(s)

Home Owners

Industry/Entity Type

Marketing

Requirements
Must have
• Company logo and contact details.

```html
<!DOCTYPE html>
<html lang="en">
<head>
<meta charset="utf-8">
<title>TV Surfacing Contractors – Brochure</title>
<link href="https://fonts.googleapis.com/css2?family=Arimo:wght@400;700&family=Questrial&display=swap" rel="stylesheet">
<style>
:root{
  --red:#e3161b;
  --black:#111111;
  --grey:#4a4a4a;
  --paper:#f4f4f4;
  --paper-edge:#d6d6d6;
  --stage:#262626;
  --blue:#3f8fe8;
}
*{margin:0;padding:0;box-sizing:border-box}
html,body{width:1200px;height:900px;overflow:hidden;background:var(--stage)}
.canvas{position:relative;width:1200px;height:900px}
.page{position:absolute;top:72px;height:754px;overflow:hidden;
  background:linear-gradient(180deg,#fafafa 0%,var(--paper) 45%,var(--paper-edge) 100%);
  box-shadow:0 6px 18px rgba(0,0,0,.55)}
.page svg.shapes{position:absolute;inset:0}
.front{left:58px;width:525px;font-family:"Arimo",Arial,sans-serif}
.back{left:622px;width:533px;font-family:"Questrial","Century Gothic",sans-serif}

/* front */
.front .hero-top{position:absolute;left:0;top:0;width:525px;height:120px;
  background:linear-gradient(90deg,#d4d6d8,#f3f3f3 35%,#f3f3f3 65%,#d4d6d8)}
.brand{position:absolute;left:167px;top:11px;width:200px;height:122px;background:#fff;
  display:flex;flex-direction:column;align-items:center;justify-content:center;gap:8px}
.brand-name{display:flex;align-items:center;gap:8px;font-weight:700;font-size:19px;color:var(--black);line-height:1.05;text-align:left}
.brand-mark{width:24px;height:24px;background:var(--blue);flex:none}
.brand-tag{font-size:10.5px;color:var(--black);text-align:center;line-height:1.25}
.front-title{position:absolute;left:0;width:525px;top:505px;text-align:center;
  color:var(--red);font-weight:700;font-size:28.5px;text-shadow:1px 1px 1px rgba(0,0,0,.25)}
.front-intro{position:absolute;left:22px;width:481px;top:542px;text-align:center;
  font-weight:700;font-size:16.3px;line-height:18.3px;color:var(--black)}
.front-url{position:absolute;left:0;width:525px;top:725px;text-align:center;color:#fff;font-weight:700;font-size:20px}

/* back */
.section-tag{position:absolute;left:50%;transform:translateX(-50%);background:var(--black);color:#fff;
  font-family:"Arimo",Arial,sans-serif;box-shadow:0 3px 5px rgba(0,0,0,.4)}
.tag-polished{top:44px;padding:6px 18px;font-size:17px;font-weight:700;letter-spacing:.3px}
.tag-contact{top:530px;width:212px;text-align:center;padding:8px 0;font-size:17px;font-weight:700}
.copy{position:absolute;left:19px;width:500px;top:92px;color:var(--grey);font-size:9.5px;line-height:11.8px}
.copy p{margin-bottom:3px}
.copy h3{font-family:"Arimo",Arial,sans-serif;font-size:12.5px;color:var(--black);font-weight:700;margin-top:2px}
.copy .lead{color:var(--red);font-size:11.2px;line-height:13px;margin-bottom:3px}
.ticks{list-style:none;margin-bottom:3px}
.ticks li{position:relative;padding-left:12px;margin-bottom:4.4px}
.ticks li::before{content:"";position:absolute;left:0;top:2px;width:7px;height:7px;background:var(--red)}
.ticks.cols{display:grid;grid-template-columns:128px 1fr;grid-auto-flow:column;grid-template-rows:repeat(4,auto)}
.contact{position:absolute;left:0;width:533px;top:580px;text-align:center;font-size:12.5px;line-height:16.4px;color:var(--black)}
.contact .strong{font-family:"Arimo",Arial,sans-serif;font-weight:700}
.contact .phone{color:var(--red);font-family:"Arimo",Arial,sans-serif;font-weight:700;display:flex;align-items:center;justify-content:center;gap:5px}
.contact .mail{display:flex;align-items:center;justify-content:center;gap:5px}
.back-url{position:absolute;left:0;width:533px;top:723px;text-align:center;color:#fff;font-size:14px;letter-spacing:10.5px}
</style>
</head>
<body>
<div class="canvas">

  <section class="page front">
    <div class="hero-top" role="img" aria-label="Faded photos of modern white homes"></div>
    <svg class="shapes" width="525" height="754" viewBox="0 0 525 754">
      <defs>
        <linearGradient id="heroTones" x1="0" y1="0" x2="1" y2="1">
          <stop offset="0" stop-color="#c9d0d6"/>
          <stop offset="0.3" stop-color="#eceeee"/>
          <stop offset="0.5" stop-color="#8d9488"/>
          <stop offset="0.68" stop-color="#4f6a45"/>
          <stop offset="0.85" stop-color="#a9a8a2"/>
          <stop offset="1" stop-color="#2f6fc8"/>
        </linearGradient>
      </defs>
      <path d="M0 112 Q262 150 525 112 L525 402 Q262 452 0 402 Z" fill="url(#heroTones)" role="img" aria-label="Photo of a modern white home with polished concrete pool patio"/>
      <path d="M0 96 Q262 150 525 108 L525 114 Q262 158 0 114 Z" fill="var(--black)"/>
      <path d="M0 400 Q262 452 525 398 L525 414 Q262 466 0 416 Z" fill="var(--red)"/>
      <circle cx="167" cy="418" r="45" fill="#6f7368" stroke="var(--red)" stroke-width="6" role="img" aria-label="Close-up of polished concrete with dark stone chip"/>
      <circle cx="370" cy="420" r="44" fill="#a39a86" stroke="var(--red)" stroke-width="6" role="img" aria-label="Close-up of polished concrete with mixed aggregate"/>
      <circle cx="261" cy="413" r="58" fill="#5a5650" stroke="var(--red)" stroke-width="7" role="img" aria-label="Polished concrete bench top with a lantern"/>
      <path d="M0 690 Q262 712 525 682 L525 686 Q262 716 0 696 Z" fill="var(--black)"/>
      <path d="M0 696 Q262 716 525 686 L525 754 L0 754 Z" fill="var(--red)"/>
    </svg>
    <div class="brand">
      <div class="brand-name"><span class="brand-mark"></span><span>TV SURFACING<br>CONTRACTORS</span></div>
      <div class="brand-tag">Concrete Grinding &amp; Polishing<br>Industrial Resin Floors</div>
    </div>
    <h1 class="front-title">TV Surfacing Contractors Limited</h1>
    <p class="front-intro">is a New Zealand owned business which has been success-fully providing Auckland with reliable Flooring Services since 2001. With over 17 year's experience as flooring specialists, our team are highly skilled when it comes to polished concrete floors; concrete block honing; concrete prepara-tion; resin floor toppings and Non slip flooring options.</p>
    <div class="front-url">www.tvsurfacing-demo.co.nz</div>
  </section>

  <section class="page back">
    <svg class="shapes" width="533" height="754" viewBox="0 0 533 754">
      <path d="M0 0 L533 0 L533 22 Q300 48 0 34 Z" fill="var(--red)"/>
      <path d="M0 34 Q300 48 533 22 L533 25 Q300 52 0 38 Z" fill="var(--black)"/>
      <path d="M0 704 Q280 700 533 684 L533 688 Q280 704 0 708 Z" fill="var(--black)"/>
      <path d="M0 708 Q280 704 533 688 L533 754 L0 754 Z" fill="var(--red)"/>
    </svg>
    <div class="section-tag tag-polished">POLISHED CONCRETE</div>
    <div class="copy">
      <p>Polished concrete has become a popular flooring choice in both new and older homes; batches; workplaces and showrooms.</p>
      <p>Polished concrete is practical, versatile and provides a classic look featuring clean lines which is durable and easy to clean.</p>
      <p>What makes polished concrete so special is that every job retains its own characteristic look with natural settlement and use of stone chip.</p>
      <p>Options are available at concrete laying stage to include coloured stone and other aggregates to create an artistic design all of your own.</p>
      <h3>The benefits of polished concrete floors</h3>
      <p class="lead">There are a number of advantages to having your concrete floors polished...</p>
      <ul class="ticks">
        <li>Low maintenance (easy to clean)</li>
        <li>Reduces dust mite and allergy problems</li>
        <li>Does not support mould growth</li>
        <li>Reduces lighting needs and improves natural lighting</li>
      </ul>
      <p>Another distinguishing feature of polished concrete is the smooth finish that we take pride in attaining to further enhance and unlock your concretes full potential.</p>
      <h3>A variety of finishes for your concrete floors</h3>
      <p class="lead">Looking to achieve a particular look with your concrete floors? We have a range of sealing products which provide different finishes for your floor, including...</p>
      <ul class="ticks">
        <li>Gloss</li>
        <li>semi-gloss</li>
        <li>matte</li>
      </ul>
      <h3>Concrete grinding and polishing for ...</h3>
      <p class="lead">Looking to achieve a particular look with your concrete floors? We have a range of sealing products which provide different finishes for your floor, including...</p>
      <ul class="ticks cols">
        <li>all interior flooring</li>
        <li>fire-hearths</li>
        <li>bench tops/vanity tops</li>
        <li>driveways</li>
        <li>walkways</li>
        <li>patios</li>
        <li>pool surrounds and any other concrete surface</li>
      </ul>
    </div>
    <div class="section-tag tag-contact">Contact details</div>
    <div class="contact">
      <div class="strong">TV SURFACING CONTRACTORS</div>
      <div class="strong">PO BOX 4021</div>
      <div>AUCKLAND 0600</div>
      <div class="phone"><svg width="11" height="11" viewBox="0 0 12 12"><rect width="12" height="12" rx="2" fill="var(--red)"/><path d="M3.5 2.5 L5 4.5 L4.2 5.5 Q5 7.2 6.6 7.9 L7.5 7 L9.5 8.5 L8.7 9.6 Q5.5 9.8 2.6 5.5 Q2.4 3.5 3.5 2.5 Z" fill="#fff"/></svg>0800 555 014</div>
      <div class="mail"><svg width="12" height="9" viewBox="0 0 12 9"><rect width="12" height="9" fill="var(--red)"/><path d="M0 0 L6 5 L12 0" stroke="#fff" fill="none"/></svg>hello@tvsurfacing-demo.co.nz</div>
      <div class="phone"><svg width="11" height="11" viewBox="0 0 12 12"><rect width="12" height="12" rx="2" fill="var(--red)"/><path d="M3.5 2.5 L5 4.5 L4.2 5.5 Q5 7.2 6.6 7.9 L7.5 7 L9.5 8.5 L8.7 9.6 Q5.5 9.8 2.6 5.5 Q2.4 3.5 3.5 2.5 Z" fill="#fff"/></svg>09 555 0192</div>
      <div>www.tvsurfacing-demo.co.nz</div>
    </div>
    <div class="back-url">www.tvsurfacing-demo.co.nz</div>
  </section>

</div>
</body>
</html>
```